BrightKeel Business Card Contest

We are looking for a modern business card that catches attention and is unique. Attached is the brand guide and logo files. Please note that the back side (not the side with our name and info) with be UV raise printed, so have fun with the design there. We want to include Name, Title, Phone number, email, website.

Contact Information for Business Card

Please see project description

```html
<!DOCTYPE html>
<html lang="en">
<head>
<meta charset="utf-8">
<title>BrightKeel Business Card</title>
<link rel="stylesheet" href="https://fonts.googleapis.com/css2?family=Montserrat:wght@500;600;700&family=Josefin+Sans:wght@400;500&display=swap">
<style>
  :root {
    --bg: #2a2c31;
    --navy: #0f1d3d;
    --navy-deep: #111a2e;
    --paper: #f3f3f1;
    --ink: #16213f;
    --muted: #7a7f8c;
    --red: #e32b1c;
    --orange: #f6821f;
    --sky: #95b9dc;
    --cyan: #1eb3ec;
    --blue: #1565d8;
    --accent-line: #22b4ea;
  }
  * { margin: 0; padding: 0; box-sizing: border-box; }
  html, body { width: 1200px; height: 900px; overflow: hidden; }
  body {
    background: var(--bg);
    font-family: "Montserrat", sans-serif;
    position: relative;
  }
  .card {
    position: absolute;
    width: 700px;
    height: 400px;
    border-radius: 6px;
    overflow: hidden;
    box-shadow: 0 18px 40px rgba(0,0,0,0.45);
  }
  .card-front { left: 80px; top: 45px; background: var(--paper); }
  .card-back { left: 420px; top: 465px; background: var(--navy-deep); }

  .front-panel {
    position: absolute; left: 0; top: 0;
    width: 315px; height: 400px;
    background: var(--navy);
  }
  .front-artwork {
    position: absolute; left: 0; bottom: 0;
    width: 315px; height: 150px;
    background: linear-gradient(160deg, var(--red) 0%, var(--orange) 30%, var(--sky) 55%, var(--cyan) 75%, var(--blue) 100%);
  }
  .brand-lockup {
    position: absolute; left: 40px; top: 140px;
    display: flex; align-items: center; gap: 12px;
  }
  .brand-square { width: 22px; height: 22px; background: var(--orange); }
  .brand-name {
    font-weight: 600; color: #ffffff; font-size: 40px; letter-spacing: -0.5px;
  }

  .front-info { position: absolute; left: 360px; top: 62px; right: 30px; }
  .person-name { font-weight: 700; font-size: 31px; color: var(--ink); }
  .person-title { font-weight: 500; font-size: 16px; color: var(--muted); margin-top: 2px; }
  .contact-list {
    list-style: none; margin-top: 30px;
    border-left: 3px solid var(--accent-line);
    padding-left: 22px;
  }
  .contact-list li {
    display: flex; align-items: center; gap: 16px;
    font-family: "Josefin Sans", sans-serif;
    font-size: 18px; color: var(--ink);
    height: 34px;
  }
  .contact-icon { width: 20px; height: 20px; fill: var(--ink); flex: none; }

  .tagline {
    position: absolute;
    font-family: "Josefin Sans", sans-serif;
    text-transform: uppercase;
    line-height: 1.55;
    white-space: nowrap;
  }
  .front-tagline { right: 50px; bottom: 52px; font-size: 11px; letter-spacing: 6px; color: #8a8e99; }
  .back-tagline { right: 60px; top: 250px; font-size: 13px; letter-spacing: 8px; color: #9aa0ad; }

  .back-artwork {
    position: absolute; left: 0; top: 0;
    width: 360px; height: 400px;
    background: linear-gradient(150deg, #2a3552 0%, #1d3f78 50%, #111a2e 100%);
  }
  .back-name {
    position: absolute; right: 60px; top: 160px;
    font-weight: 600; font-size: 50px; color: #f4f4f4; letter-spacing: -0.5px;
  }
</style>
</head>
<body>

<section class="card card-front" aria-label="Business card front">
  <div class="front-panel">
    <div class="front-artwork" role="img" aria-label="Decorative area of angled brand colour bands in red, orange and blues"></div>
    <div class="brand-lockup">
      <span class="brand-square"></span>
      <span class="brand-name">BrightKeel</span>
    </div>
  </div>

  <div class="front-info">
    <h1 class="person-name">Jordan Hale</h1>
    <p class="person-title">Business Development Manager</p>
    <ul class="contact-list">
      <li>
        <svg class="contact-icon" viewBox="0 0 24 24" aria-hidden="true"><path d="M6.6 10.8a15.1 15.1 0 0 0 6.6 6.6l2.2-2.2a1 1 0 0 1 1-.25 11.4 11.4 0 0 0 3.6.57 1 1 0 0 1 1 1V20a1 1 0 0 1-1 1A17 17 0 0 1 3 4a1 1 0 0 1 1-1h3.5a1 1 0 0 1 1 1c0 1.25.2 2.45.57 3.6a1 1 0 0 1-.25 1z"/></svg>
        (555) 318-7240
      </li>
      <li>
        <svg class="contact-icon" viewBox="0 0 24 24" aria-hidden="true"><path d="M2 5h20v14H2z M4 7v.4l8 5 8-5V7l-8 5z" fill-rule="evenodd"/></svg>
        jordan@brightkeel.com
      </li>
      <li>
        <svg class="contact-icon" viewBox="0 0 24 24" aria-hidden="true"><circle cx="12" cy="12" r="9" fill="none" stroke="var(--ink)" stroke-width="1.6"/><ellipse cx="12" cy="12" rx="4" ry="9" fill="none" stroke="var(--ink)" stroke-width="1.4"/><path d="M3 12h18M4.5 7.5h15M4.5 16.5h15" stroke="var(--ink)" stroke-width="1.3"/></svg>
        www.brightkeel.com
      </li>
    </ul>
  </div>

  <p class="tagline front-tagline">Steering<br>a steadier<br>course</p>
</section>

<section class="card card-back" aria-label="Business card back">
  <div class="back-artwork" role="img" aria-label="Raised UV artwork area in metallic red, silver and blue tones"></div>
  <div class="back-name">BrightKeel</div>
  <p class="tagline back-tagline">Steering<br>a steadier<br>course</p>
</section>

</body>
</html>
```